Coffee bag stamp design for new coffee brand

Stamp design that will be used like a label on a coffee package.
It must be a vector that can be produced as a stamp. Coffee bag is from brown craft paper. I upload image of this bag. Size of design is 80mm x 140mm.
I also uploaded two pictures for inspiration, but I will also appreciate new ideas.

Target Market(s)

Coffee lovers, who love to try new coffee. Also hipsters.

Colors

Designer to choose only greyscale colors for use in the design.

Requirements
Must have
• Some information about coffee must have:
Name: BRAZIL (the biggest font in that design)
Region: Santos
Altitude: 60 – 1200 m.n.m.
Variety: Arabica
Processing: unwashed

```html
<!DOCTYPE html>
<html lang="en">
<head>
<meta charset="utf-8">
<title>Brazil Santos – Coffee Bag Stamp</title>
<link href="https://fonts.googleapis.com/css2?family=Federo&family=Roboto+Condensed:wght@400;700&display=swap" rel="stylesheet">
<style>
  :root {
    --ink: #2b2b2b;
    --ink-soft: #d9d9d9;
    --ink-mid: #9a9a9a;
    --background: #ffffff;
  }
  * { box-sizing: border-box; margin: 0; padding: 0; }
  html, body {
    width: 1200px; height: 1000px; overflow: hidden;
    background: var(--background);
  }
  .canvas { position: relative; width: 1200px; height: 1000px; }
  .stamp {
    position: absolute; left: 380px; top: 62px;
    width: 440px; height: 880px; color: var(--ink);
  }
  .stamp-lines { position: absolute; inset: 0; }
  .brand {
    position: absolute; left: 0; top: 40px; width: 100%;
    display: flex; justify-content: center; align-items: center; gap: 10px;
  }
  .brand-dot { width: 18px; height: 18px; border: 3px solid var(--ink); border-radius: 50%; }
  .brand-name {
    font-family: "Federo", sans-serif; font-size: 26px; letter-spacing: 1px;
    color: var(--ink); line-height: 1;
  }
  .emblem {
    position: absolute; left: 40px; top: 150px; width: 360px; height: 300px;
    border-radius: 50% 50% 18px 18px;
    background: radial-gradient(ellipse at 50% 55%, var(--ink-mid) 0%, var(--ink-soft) 55%, var(--background) 100%);
  }
  .origin-name {
    position: absolute; left: 0; top: 472px; width: 100%; text-align: center;
    font-family: "Federo", sans-serif; font-size: 76px; line-height: 1;
    letter-spacing: 3px; font-weight: 400;
    -webkit-text-stroke: 1.5px var(--ink);
  }
  .origin-region {
    position: absolute; left: 0; top: 560px; width: 100%; text-align: center;
    font-family: "Federo", sans-serif; font-size: 40px; line-height: 1;
    letter-spacing: 3px; -webkit-text-stroke: 0.6px var(--ink);
  }
  .facts {
    position: absolute; left: 0; top: 648px; width: 100%;
    display: grid; grid-template-columns: repeat(3, 1fr);
    font-family: "Roboto Condensed", sans-serif; text-align: center;
  }
  .fact-label { font-size: 19px; font-weight: 400; }
  .fact-icon { display: block; margin: 10px auto 9px; }
  .fact-value { font-size: 19px; font-weight: 700; }
  .weights {
    position: absolute; left: 0; top: 834px; width: 100%;
    display: flex; justify-content: center; gap: 28px;
    font-family: "Roboto Condensed", sans-serif; font-weight: 700; font-size: 19px;
  }
  .weight { display: flex; align-items: center; gap: 7px; }
  .weight-box { width: 16px; height: 16px; border: 2px solid var(--ink); }
</style>
</head>
<body>
<main class="canvas">
  <section class="stamp">
    <svg class="stamp-lines" width="440" height="880" viewBox="0 0 440 880" fill="none" stroke="var(--ink)" stroke-width="3">
      <g class="brand-rules">
        <line x1="0" y1="38" x2="108" y2="38"/><line x1="0" y1="55" x2="96" y2="55"/><line x1="0" y1="72" x2="108" y2="72"/>
        <line x1="332" y1="38" x2="440" y2="38"/><line x1="344" y1="55" x2="440" y2="55"/><line x1="332" y1="72" x2="440" y2="72"/>
      </g>
      <g class="region-rules">
        <line x1="0" y1="562" x2="70" y2="562"/><line x1="0" y1="578" x2="50" y2="578"/><line x1="0" y1="594" x2="70" y2="594"/>
        <line x1="370" y1="562" x2="440" y2="562"/><line x1="390" y1="578" x2="440" y2="578"/><line x1="370" y1="594" x2="440" y2="594"/>
      </g>
      <line x1="0" y1="628" x2="440" y2="628"/>
      <line x1="148" y1="646" x2="148" y2="772"/>
      <line x1="292" y1="646" x2="292" y2="772"/>
      <line x1="0" y1="796" x2="440" y2="796"/>
    </svg>

    <div class="brand">
      <span class="brand-dot"></span>
      <span class="brand-name">KESTREL ROAST</span>
    </div>

    <div class="emblem" role="img" aria-label="Line illustration of a stylised bird with spread wings on coffee branches, under a rising sun with rays and stars"></div>

    <h1 class="origin-name">BRAZIL</h1>
    <h2 class="origin-region">SANTOS</h2>

    <div class="facts">
      <div class="fact">
        <p class="fact-label">Processing:</p>
        <svg class="fact-icon" width="50" height="50" viewBox="0 0 50 50" fill="none" stroke="var(--ink)" stroke-width="2.5">
          <circle cx="25" cy="25" r="22"/>
          <line x1="12" y1="31" x2="38" y2="31"/>
          <circle cx="17" cy="26" r="3"/><circle cx="25" cy="26" r="3"/><circle cx="33" cy="26" r="3"/>
          <line x1="25" y1="13" x2="25" y2="20"/><line x1="21" y1="16" x2="29" y2="16"/>
        </svg>
        <p class="fact-value">Unwashed</p>
      </div>
      <div class="fact">
        <p class="fact-label">Altitude:</p>
        <svg class="fact-icon" width="50" height="50" viewBox="0 0 50 50" fill="none" stroke="var(--ink)" stroke-width="2.5">
          <circle cx="25" cy="25" r="22"/>
          <polyline points="10,32 20,19 25,25 30,17 40,32" stroke-linejoin="round"/>
        </svg>
        <p class="fact-value">60 – 1200</p>
      </div>
      <div class="fact">
        <p class="fact-label">Variety:</p>
        <svg class="fact-icon" width="50" height="50" viewBox="0 0 50 50" fill="none" stroke="var(--ink)" stroke-width="2.5">
          <circle cx="25" cy="25" r="22"/>
          <ellipse cx="21" cy="26" rx="6" ry="9" fill="var(--ink)" transform="rotate(-15 21 26)"/>
          <ellipse cx="30" cy="24" rx="6" ry="9" fill="var(--ink)" transform="rotate(-15 30 24)"/>
        </svg>
        <p class="fact-value">Arabica</p>
      </div>
    </div>

    <div class="weights">
      <span class="weight"><span class="weight-box"></span>100 g</span>
      <span class="weight"><span class="weight-box"></span>250 g</span>
      <span class="weight"><span class="weight-box"></span>500 g</span>
      <span class="weight"><span class="weight-box"></span>1000 g</span>
    </div>
  </section>
</main>
</body>
</html>
```